5 x Packaging Design - Most of the design style is already done!

The logo is "Fern And Flint" which will remain the same. The font is Athens.

We just require realistic packaging design with the fronts of the packaging. Together/ seperate/ in different mockup backdrops etc.

CLAY MASKS: BLACK JAR WHITE LID:
- the cursive coloured font is "Majesty"
- If you think you can design something even more attractive go for it! but we like the design a lot.
- Most important for us is to make it look realistic on the packaging so that we can use it on the website :)

BEARD OIL: BLACK JAR WITH SILVER AND WHITE PUMP LID:
- You are free to design similar/same or completely different

competitors:
Morvelle
reedandrain

Industry/Entity Type

Cosmetics

```html
<!DOCTYPE html>
<html lang="en">
<head>
<meta charset="utf-8">
<title>Fern And Flint – Packaging Fronts</title>
<link rel="stylesheet" href="https://fonts.googleapis.com/css2?family=Josefin+Sans:wght@300&family=Caveat+Brush&family=Pacifico&family=Space+Mono&family=Oswald:wght@400&display=swap">
<style>
  :root {
    --backdrop: #ecebe8;
    --jar-black: #0d0d0d;
    --lid-white: #f6f6f4;
    --lid-shade: #dcdcda;
    --label-white: #eaeaea;
    --accent-red: #d0202a;
    --accent-pink: #e04aa6;
    --accent-lime: #7bc62d;
    --accent-gold: #f2c318;
    --pump-silver: #b9bcc0;
    --pump-stem: #9a9ea2;
    --pump-ring: #8d9094;
    --pump-clear: #d9dde0;
  }
  * { margin: 0; padding: 0; box-sizing: border-box; }
  html, body { width: 1200px; height: 675px; overflow: hidden; }
  body { background: var(--backdrop); position: relative; }

  .jar { position: absolute; top: 210px; width: 210px; }
  .jar-lid {
    height: 92px; background: linear-gradient(180deg, var(--lid-white), var(--lid-shade));
    border-radius: 14px 14px 4px 4px;
  }
  .jar-body {
    height: 190px; margin-top: 4px; background: var(--jar-black);
    border-radius: 4px 4px 14px 14px; text-align: center; padding: 20px 12px 0;
    color: var(--label-white);
  }
  .brand-name {
    font-family: "Josefin Sans", sans-serif; font-weight: 300;
    font-size: 13px; letter-spacing: 3px; text-transform: uppercase; white-space: nowrap;
  }
  .product-name {
    font-family: "Caveat Brush", cursive; font-size: 28px; line-height: 0.9;
    margin: 14px 0 8px; text-transform: uppercase;
  }
  .product-type, .product-benefit, .product-volume {
    font-family: "Space Mono", monospace; text-transform: uppercase;
  }
  .product-type { font-size: 11px; letter-spacing: 2px; line-height: 1.3; }
  .product-benefit { font-size: 7px; letter-spacing: 1px; line-height: 1.4; margin-top: 4px; }
  .product-volume { font-size: 7px; margin-top: 4px; }

  .ember-root   { left: 40px; }  .ember-root .product-name { color: var(--accent-red); }
  .rose-hush    { left: 275px; } .rose-hush .product-name { color: var(--accent-pink); }
  .verdant-calm { left: 510px; } .verdant-calm .product-name { color: var(--accent-lime); }
  .golden-hour  { left: 745px; } .golden-hour .product-name { color: var(--accent-gold); }

  .bottle { position: absolute; left: 1000px; top: 110px; width: 150px; }
  .bottle-pump { display: block; margin: 0 auto; }
  .bottle-body {
    height: 300px; background: var(--jar-black); border-radius: 38px 38px 12px 12px;
    color: var(--label-white); text-align: center; padding-top: 46px;
  }
  .bottle-body .brand-name { font-size: 11px; letter-spacing: 2px; }
  .bottle-rule { border-top: 2px solid var(--label-white); margin: 10px 14px; }
  .bottle-tag { font-family: "Oswald", sans-serif; font-size: 13px; text-transform: uppercase; }
  .bottle-title { font-family: "Pacifico", cursive; font-size: 28px; line-height: 1.6; }
  .bottle-scent { font-family: "Oswald", sans-serif; font-size: 17px; text-transform: uppercase; margin-top: 14px; }
  .bottle-volume { font-family: "Oswald", sans-serif; font-size: 10px; margin-top: 30px; }
</style>
</head>
<body>
  <div class="jar ember-root">
    <div class="jar-lid"></div>
    <div class="jar-body">
      <p class="brand-name">Fern And Flint</p>
      <p class="product-name">Ember<br>Root</p>
      <p class="product-type">Green<br>Clay Mask</p>
      <p class="product-benefit">Moisturising and<br>skin rejuvenating</p>
      <p class="product-volume">50ml</p>
    </div>
  </div>

  <div class="jar rose-hush">
    <div class="jar-lid"></div>
    <div class="jar-body">
      <p class="brand-name">Fern And Flint</p>
      <p class="product-name">Rose<br>Hush</p>
      <p class="product-benefit">Exfoliating &amp; pore refining</p>
      <p class="product-type">Pink<br>Clay Cream Mask</p>
      <p class="product-volume">50ml</p>
    </div>
  </div>

  <div class="jar verdant-calm">
    <div class="jar-lid"></div>
    <div class="jar-body">
      <p class="brand-name">Fern And Flint</p>
      <p class="product-name">Verdant<br>Calm</p>
      <p class="product-type">Green<br>Clay Mask</p>
      <p class="product-benefit">Pore tightening</p>
      <p class="product-volume">50ml</p>
    </div>
  </div>

  <div class="jar golden-hour">
    <div class="jar-lid"></div>
    <div class="jar-body">
      <p class="brand-name">Fern And Flint</p>
      <p class="product-name">Golden<br>Hour</p>
      <p class="product-type">Turmeric<br>Clay Cream Mask</p>
      <p class="product-benefit">Anti-inflammatory<br>and detoxifying</p>
      <p class="product-volume">50ml</p>
    </div>
  </div>

  <div class="bottle">
    <svg class="bottle-pump" width="80" height="180" viewBox="0 0 80 180" aria-hidden="true">
      <rect x="22" y="0" width="36" height="95" rx="4" fill="var(--pump-clear)"/>
      <rect x="30" y="10" width="20" height="60" fill="var(--pump-stem)"/>
      <rect x="16" y="95" width="48" height="85" rx="3" fill="var(--pump-silver)"/>
      <rect x="16" y="120" width="48" height="4" fill="var(--pump-ring)"/>
    </svg>
    <div class="bottle-body">
      <p class="brand-name">Fern And Flint</p>
      <div class="bottle-rule"></div>
      <p class="bottle-tag">Premium Organic</p>
      <div class="bottle-rule"></div>
      <p class="bottle-title">Beard Oil</p>
      <div class="bottle-rule"></div>
      <p class="bottle-scent">Patchouli</p>
      <p class="bottle-volume">30ML</p>
    </div>
  </div>
</body>
</html>
```